Larkfield Clinic Marketing Flyer

We are a new medical practice in the community and need a flyer to send to other medical offices to inform of our services. We just completed our logo with PixelGuild and would like to incorporate that plus our marketing content into the flyer. Our medical practice has 2 divisions: (1)Mental Health/Psychiatry and (2) Migraine and Neurospasticity Management. Please see website for content and provider photos at www.LarkfieldCare.example

Target Market(s)

Other Healthcare Professionals in the Community

Industry/Entity Type

Medical

Requirements
Must have
• Photos of all 5 healthcare providers, phone number, address, logo

```html
<!DOCTYPE html>
<html lang="en">
<head>
<meta charset="utf-8">
<title>Larkfield Clinic Flyer</title>
<link href="https://fonts.googleapis.com/css2?family=Nunito+Sans:ital,wght@0,400;0,600;0,700;0,800;0,900;1,700&display=swap" rel="stylesheet">
<style>
:root{
  --teal-dark:#0b5e53;
  --teal:#0f6e61;
  --teal-band:#148a77;
  --lime:#92c83e;
  --light:#eef5ec;
  --white:#ffffff;
  --ink:#1f2a28;
  --stage:#d9d6d0;
}
*{margin:0;padding:0;box-sizing:border-box}
html,body{width:1200px;height:900px;overflow:hidden;background:var(--stage);font-family:"Nunito Sans",sans-serif}
.flyer{position:absolute;left:296px;top:20px;width:608px;height:860px;overflow:hidden;background:var(--teal)}
.hero{position:absolute;left:0;top:0;width:608px;height:300px;background:linear-gradient(135deg,#0d6a5d 0%,#14806f 55%,#0c5f54 100%)}
.hero-photo{position:absolute;left:250px;top:40px;width:358px;height:230px;background:radial-gradient(ellipse at 50% 45%,rgba(120,190,170,.35),rgba(15,110,97,0) 70%)}
.logo-tab{position:absolute;left:487px;top:0;width:83px;height:78px;background:var(--white);border-radius:0 0 12px 12px;display:flex;align-items:center;justify-content:center;gap:4px;flex-direction:column}
.logo-tab .dot{width:14px;height:14px;border-radius:50%;background:var(--teal-band)}
.logo-tab .name{font-size:9px;font-weight:800;color:var(--teal-band);text-align:center;line-height:1.1}
.headline{position:absolute;left:54px;top:72px;font-size:40px;line-height:53px;color:var(--white);font-weight:400;letter-spacing:.3px}
.headline b{color:var(--lime);font-weight:900}
.tagline{position:absolute;left:49px;top:228px;font-size:12.5px;font-style:italic;font-weight:700;color:var(--white)}
.providers{position:absolute;left:0;top:270px;width:608px;height:285px;background:var(--light)}
.providers-curve{position:absolute;left:0;top:250px}
.meet{position:absolute;left:49px;top:292px;font-size:29px;line-height:36px;color:var(--teal-dark);font-weight:400}
.meet b{color:var(--lime);font-weight:900;display:block}
.services-box{position:absolute;left:345px;top:208px;width:229px;height:174px;background:var(--teal-band);border-radius:18px;box-shadow:4px 5px 0 var(--lime);padding:12px 10px 10px 12px;color:var(--white)}
.services-box li{list-style:none;position:relative;padding-left:11px;margin-bottom:6px}
.services-box li::before{content:"";position:absolute;left:0;top:3px;width:7px;height:7px;border-radius:50%;background:var(--lime)}
.services-box h4{font-size:8.8px;font-weight:700}
.services-box p{font-size:7.6px;line-height:12px;padding-left:2px}
.team{position:absolute;left:49px;top:420px;display:flex;gap:15px}
.member{width:89px;text-align:center;font-size:9px;color:var(--ink);line-height:11px}
.member .photo{width:89px;height:89px;margin-bottom:10px;background:radial-gradient(circle at 50% 35%,#8a8f8c,#3a4240)}
.member .photo.warm{background:radial-gradient(circle at 50% 35%,#c9a47a,#6b5038)}
.member strong{font-weight:700;display:block}
.practice{position:absolute;left:0;top:552px;width:608px;height:220px;background:linear-gradient(160deg,#0d6659,#0a574d)}
.practice h2{position:absolute;left:49px;top:14px;font-size:30px;font-weight:400;color:var(--lime);letter-spacing:.3px}
.practice h2 b{font-weight:900}
.practice h3{position:absolute;left:49px;font-size:13.5px;font-weight:600;color:var(--lime)}
.practice .text{position:absolute;left:63px;top:81px;width:510px;font-size:9.6px;line-height:16px;color:var(--white)}
.conditions{position:absolute;left:62px;top:170px;display:grid;grid-template-columns:125px 222px 140px;row-gap:8px;font-size:9.6px;color:var(--white)}
.conditions span{position:relative;padding-left:13px}
.conditions span::before{content:"";position:absolute;left:0;top:3px;width:7px;height:7px;border-radius:50%;background:var(--lime)}
.contact{position:absolute;left:0;top:772px;width:608px;height:88px;background:var(--teal-band)}
.contact .label{position:absolute;left:54px;top:16px;font-size:18px;font-weight:700;color:var(--lime)}
.contact .phones{position:absolute;left:54px;top:43px;font-size:19.5px;font-weight:700;color:var(--white)}
.contact .address{position:absolute;left:385px;top:14px;font-size:10px;line-height:15px;color:var(--white);padding-left:14px}
.contact .address svg{position:absolute;left:0;top:2px}
.contact .email{position:absolute;left:383px;top:52px;font-size:9.6px;color:var(--white);border:1px solid var(--white);border-radius:10px;padding:1px 7px}
</style>
</head>
<body>
<main class="flyer">
  <section class="hero">
    <div class="hero-photo" role="img" aria-label="Photo of clasped hands in a caring gesture, tinted teal"></div>
  </section>
  <svg class="providers-curve" width="608" height="60" viewBox="0 0 608 60" aria-hidden="true">
    <path d="M0 20 H520 C570 20 590 10 608 -5 V60 H0 Z" fill="var(--light)"/>
    <path d="M560 60 C590 40 600 20 608 0" stroke="var(--lime)" stroke-width="3" fill="none"/>
  </svg>
  <section class="providers">
    <svg width="608" height="285" aria-hidden="true" style="position:absolute;left:0;top:0">
      <path d="M0 150 C150 130 300 150 608 110" stroke="#dfeadb" stroke-width="14" fill="none"/>
      <path d="M0 190 C200 170 380 175 608 140" stroke="#e4eee1" stroke-width="10" fill="none"/>
    </svg>
  </section>
  <div class="logo-tab"><span class="dot"></span><span class="name">Larkfield Clinic</span></div>
  <h1 class="headline">WE CARE <b>ABOUT</b><br><b>YOUR BODY, MIND,</b><br>AND <b>HEALTH.</b></h1>
  <p class="tagline">Board Certified. Responsive. Compassionate.</p>
  <ul class="services-box">
    <li><h4>New Patient Evaluation</h4><p>Consults provided for evaluation and management of patients with chronic migraines or neurospasticity challenges.</p></li>
    <li><h4>Insurance Pre-Authorization</h4><p>Botulinum toxin injections may be a recommended treatment option. If so, our office completes insurance pre-authorizations on your behalf.</p></li>
    <li><h4>Follow-Up Appointments</h4><p>Timely appointments following insurance approval are available to quickly get you on the road to relief.</p></li>
  </ul>
  <h2 class="meet">MEET OUR<b>HEALTHCARE</b><b>PROVIDERS</b></h2>
  <div class="team">
    <div class="member"><div class="photo warm" role="img" aria-label="Portrait photo of Dr. Alan Whitcombe"></div><strong>Dr. Alan Whitcombe</strong></div>
    <div class="member"><div class="photo" role="img" aria-label="Portrait photo of Owen Marsh"></div><strong>Owen Marsh</strong>PMHNP - BC</div>
    <div class="member"><div class="photo" role="img" aria-label="Portrait photo of Clara Bennet"></div><strong>Clara Bennet</strong>PMHNP - BC</div>
    <div class="member"><div class="photo" role="img" aria-label="Portrait photo of Neil Harlow"></div><strong>Neil Harlow</strong>PMHNP - BC</div>
    <div class="member"><div class="photo" role="img" aria-label="Portrait photo of Ruth Ellery"></div><strong>Ruth Ellery</strong>PMHNP - BC</div>
  </div>
  <section class="practice">
    <h2><span style="color:var(--lime)">OUR</span> <b>MEDICAL PRACTICE</b></h2>
    <h3 style="top:57px">1. Migraine and Neurospasticity Intervention:</h3>
    <p class="text">Injections of botulinum neurotoxin are a widely used therapeutic form of treatment for both chronic migraines and patients with involuntary muscle contractions (neurospasticity). Injections may offer up to 3 months of relief and may be combined with other pharmaceutical interventions for maximum benefit.</p>
    <h3 style="top:142px">2. Mental Health and Psychiatry Services:</h3>
    <div class="conditions">
      <span>Bipolar Disorder</span><span>Moderate, Minor and Major Depression</span><span>Schizophrenia</span>
      <span>ADD/ADHD</span><span>Stress or Grief Reactions</span><span>Anxiety and others</span>
    </div>
  </section>
  <footer class="contact">
    <p class="label">Contact us for more info:</p>
    <p class="phones">(555) 014-2206 • (555) 014-2286</p>
    <p class="address"><svg width="8" height="11" viewBox="0 0 8 11" aria-hidden="true"><path d="M4 0C1.8 0 0 1.7 0 3.9 0 6.8 4 11 4 11s4-4.2 4-7.1C8 1.7 6.2 0 4 0zm0 5.3a1.4 1.4 0 1 1 0-2.8 1.4 1.4 0 0 1 0 2.8z" fill="#fff"/></svg>312 Maple Row, Suite B<br>Brookhaven, ID 83000</p>
    <p class="email">support@LarkfieldCare.example</p>
  </footer>
</main>
</body>
</html>
```